Web Design Project for Weightwise Alliance

Aim
As the peak body on obesity, to be the ‘go to website’ for information about obesity and for people that are overweight or obese. Whether an individual looking for support and advice; a professional such as a dietician or a medical practitioner; an academic researcher studying the field; a related organisation specialising in cancer; diabetes or cardio issues or a policy maker
Requirements
A professional site that is compatible for viewing on PCs Mac, ipads and iphones
To include the following:
• Announcements bar – (for adding in conferences, news grabs etc)
• Search tool (for academic’s papers, terms in fact sheets)
• Secure log in (for KRP & WA directors & staff personnel for board papers etc)
• Good visuals including changing photos (should be engaging for public – see sample)
• Web sharing apps Email/facebook login and other social media; like button
• Get involved – to express interest in conferences; potential sponsors
• Ebulletin (KRP)- subscribe - emailed to a database or posted to a social media site
• WA Recommended Apps - DLQ, VORN, Plateloggr? T&K
• WA blog
• Capture database of emails/enquiries for ebulletin and fact sheets
Contents
Landing page – containing aspects above (announcements, search tool, visuals, social media tools, get involved button, recommended apps);
Mission statement and logo with words ‘insight and momentum’ prominently displayed
Sections
1. About WA - Who we are – Weightwise Alliance Board and Expert Review Panel cvs; CEO and research officer – annual report
2. For General Public - The big questions about obesity – the interaction of food (protein & fructose), exercise, epigenetics “its not your fault”, hormones (eg leptin) & metabolism. The Fact Sheets; simple summaries of latest research?
3. For Professionals - Expert Review Panel - KRP Ebulletins - Research and Publications
4. Media and latest news on obesity
5. Support WA in its mission– get involved – note DGR status etc.
6. Website terms of use – Halvers to provide disclaimers etc
For later - professionals – Post Conference youtubes
- general public – anti-obesity app
Websites we like:
- http://www.sugarscalehub.com
- www.bellytrust.org.au
- http://www.tallo.org/international - clean lines; well organised
- http://www.verdal.org/ good layout of tabs about us, news and media, science, login, myverdalpage
- http://www.rallyzone.co.uk/sport innovate way to promote fitness
We would also be keen to get the site coded so would like an estimate of how much it would cost to create the html version of the site also with css for the main styles.

```html
<!DOCTYPE html>
<html lang="en">
<head>
<meta charset="utf-8">
<title>Weightwise Alliance — Home</title>
<link rel="stylesheet" href="https://fonts.googleapis.com/css2?family=Open+Sans:wght@400;600&display=swap">
<style>
:root{
  --navy:#0a3a8c;
  --navy-deep:#062c73;
  --teal:#14b8cc;
  --teal-soft:#d9f6fa;
  --ink:#333333;
  --heading:#666666;
  --muted:#777777;
  --line:#dddddd;
  --field:#e9ecf1;
  --field-border:#c9ccd2;
  --page:#ffffff;
}
*{box-sizing:border-box;margin:0;padding:0}
html,body{width:1200px;height:1122px;overflow:hidden;background:var(--page)}
body{position:relative;font-family:"Open Sans",Arial,sans-serif;color:var(--ink)}
.abs{position:absolute}

/* header */
.brand-mark{left:132px;top:20px;width:66px;height:66px;border-radius:50%;background:var(--navy)}
.brand-name{left:34px;top:96px;font-size:31px;font-weight:400;color:var(--teal);letter-spacing:.3px;white-space:nowrap}
.brand-tagline{left:36px;top:132px;font-size:15px;color:var(--navy);letter-spacing:2.4px;white-space:nowrap}
.search{left:868px;top:85px;width:299px;height:31px;border:1px solid var(--field-border);background:#fff}
.search span{position:absolute;left:12px;top:5px;font-size:15px;font-style:italic;font-weight:600;color:#d4d8de;letter-spacing:1px}
.search svg{position:absolute;right:8px;top:6px}

/* navigation */
.nav{left:325px;top:131px;width:844px;height:40px;background:linear-gradient(#0d4aa6,var(--navy-deep));border-radius:3px 3px 0 0}
.nav-rule{left:21px;top:167px;width:1159px;height:4px;background:var(--navy-deep)}
.nav ul{list-style:none;display:flex;height:100%;padding-left:5px}
.nav li{font-size:15px;color:#fff;padding:0 19px;line-height:40px;white-space:nowrap}
.nav li.current{background:#e6e9ee;color:var(--navy);margin-top:6px;line-height:34px;padding:0 17px}

/* hero */
.hero-photo{left:17px;top:171px;width:1164px;height:433px;background:linear-gradient(90deg,#eceef1 0%,#f2f3f5 35%,#e3e5ea 70%,#d6d9e0 100%)}
.hero-line{left:681px;white-space:nowrap;letter-spacing:1.5px}
.hero-line.primary{top:320px;font-size:42px;color:var(--navy)}
.hero-line.secondary{top:368px;font-size:37px;color:#6b6b6b}

/* columns */
.col-heading{font-size:28px;color:var(--heading);font-weight:400;top:628px}
.divider{top:638px;height:381px;border-left:2px dotted #9a9a9a}
.label{font-size:16px;color:var(--ink)}
.field{background:var(--field);border:1px solid var(--field-border);border-radius:2px}
.btn{background:linear-gradient(#1453b5,var(--navy-deep));color:#fff;font-size:17px;text-align:center;border-radius:3px}
.forgot{left:142px;top:805px;font-size:12px;color:var(--ink);display:flex;align-items:center;gap:5px}
.forgot i{display:inline-block;width:11px;height:11px;border:1px solid #aaa}

.ebulletin{left:21px;top:876px;width:358px;height:130px;border:1px solid #6fd3df;border-radius:3px;background:linear-gradient(#f3fdfe,var(--teal-soft) 40%,var(--teal))}
.ebulletin h3{position:absolute;left:16px;top:14px;font-size:21px;font-weight:400;color:#444}
.ebulletin .hint{position:absolute;left:20px;top:99px;font-size:14px;color:#3a6b70}

.about-photo{left:421px;top:677px;width:344px;height:129px;background:linear-gradient(90deg,#7e8f9a,#b08a72 35%,#c49a80 55%,#8fa6b4)}
.about-text{left:421px;top:820px;width:344px;font-size:15.4px;line-height:21.4px;color:var(--ink)}
.read-more{font-size:14px;color:var(--navy)}

.post{left:809px;width:371px;border-bottom:1px solid var(--line)}
.post h4{font-size:16px;font-weight:400;line-height:23.5px;color:#333;letter-spacing:.2px}
.post p{font-size:13.5px;line-height:18px;color:var(--muted);letter-spacing:.4px}

/* footer */
.footer-rule{left:21px;top:1067px;width:1159px;height:1px;background:var(--line)}
.footer-text{left:35px;top:1084px;font-size:13px;color:var(--muted);letter-spacing:.3px}
.social{left:1104px;top:1082px;display:flex;gap:5px}
.social i{width:22px;height:22px;border-radius:50%;background:#d0d0d0;display:block}
.footer-band{left:0;top:1116px;width:1200px;height:6px;background:var(--navy-deep)}
</style>
</head>
<body>

<header>
  <div class="abs brand-mark" aria-hidden="true"></div>
  <div class="abs brand-name">Weightwise Alliance</div>
  <div class="abs brand-tagline">insight and momentum</div>
  <div class="abs search">
    <span>SEARCH</span>
    <svg width="20" height="20" viewBox="0 0 20 20" aria-hidden="true"><circle cx="8" cy="8" r="6" fill="none" stroke="#555" stroke-width="2"/><line x1="12.5" y1="12.5" x2="18" y2="18" stroke="#555" stroke-width="2.4" stroke-linecap="round"/></svg>
  </div>
  <nav class="abs nav">
    <ul>
      <li class="current">Home</li>
      <li>About WA</li>
      <li>Who we are</li>
      <li>For General Public</li>
      <li>For Professionals</li>
      <li>Media &amp; Latest News</li>
    </ul>
  </nav>
  <div class="abs nav-rule"></div>
</header>

<section>
  <div class="abs hero-photo" role="img" aria-label="Photo of a white bathroom scale with a stethoscope lying across it"></div>
  <div class="abs hero-line primary">LOOSE YOUR WEIGHT</div>
  <div class="abs hero-line secondary">KEEP YOURSELF HEALTHY</div>
</section>

<main>
  <!-- member login -->
  <h2 class="abs col-heading" style="left:21px">Member Login</h2>
  <div class="abs label" style="left:45px;top:700px">Username :</div>
  <div class="abs field" style="left:142px;top:696px;width:236px;height:31px"></div>
  <div class="abs label" style="left:49px;top:750px">Password :</div>
  <div class="abs field" style="left:142px;top:746px;width:236px;height:31px"></div>
  <div class="abs forgot"><i></i>Forgot Password ?</div>
  <div class="abs btn" style="left:284px;top:799px;width:94px;height:28px;line-height:28px">Login</div>

  <div class="abs ebulletin">
    <h3>Ebulletin Subscribe</h3>
    <div class="abs field" style="left:19px;top:60px;width:234px;height:32px;background:#eef0f3"></div>
    <div class="abs btn" style="left:257px;top:62px;width:86px;height:28px;line-height:28px">Submit</div>
    <div class="hint">Enter your email Id</div>
  </div>

  <div class="abs divider" style="left:399px"></div>

  <!-- about -->
  <h2 class="abs col-heading" style="left:421px">About WA</h2>
  <div class="abs about-photo" role="img" aria-label="Photo of an overweight man in swim shorts at the beach, seen from the side"></div>
  <p class="abs about-text">Lorem Ipsum is simply dummy text of the printing and typesetting industry. Lorem Ipsum has been the industry's standard dummy text ever since the 1500s, when an unknown printer took a galley of type and scrambled it to make a type specimen book.</p>
  <div class="abs read-more" style="left:688px;top:972px">Read more</div>

  <div class="abs divider" style="left:785px"></div>

  <!-- blog -->
  <h2 class="abs col-heading" style="left:807px">One Blog</h2>
  <article class="abs post" style="top:670px;height:101px">
    <h4>Let’s celebrate immunization week without easing up the effort</h4>
    <p>APR, 27 2012</p><p>Posted by Guest Blogger</p>
  </article>
  <article class="abs post" style="top:782px;height:103px">
    <h4>Let’s celebrate immunization week without easing up the effort</h4>
    <p>APR, 27 2012</p><p>Posted by Guest Blogger</p>
  </article>
  <article class="abs post" style="top:896px;height:100px">
    <h4>Let’s celebrate immunization week without easing up the effort</h4>
    <p>APR, 27 2012</p><p>Posted by Guest Blogger</p>
  </article>
  <div class="abs read-more" style="left:1107px;top:1001px">Read more</div>
</main>

<footer>
  <div class="abs footer-rule"></div>
  <div class="abs footer-text">©2012 WA - Terms of Service - Privacy Policy - Program Policies</div>
  <div class="abs social" aria-label="Social links"><i></i><i></i><i></i></div>
  <div class="abs footer-band"></div>
</footer>

</body>
</html>
```